Box for a Bold Bathroom - stylish minimalist package for a modern upscale brand

We need an adaptable package design using a color label on a brown box, or just a brown box with 2 or 3 color printing. The best design would be one that is adaptable for either use.

Our first products launching under this brand will be a series of medicine cabinets and mirrors, and our cartons can vary in size from 500x100x600 mm to 1200x300x1000 mm

About us: we produce a variety of bathroom fixtures including medicine cabinets, mirrors, vanities, etc. You've likely seen our products - we do manufacturing for Valdrane, Murtello, Fenwick Hollow, Dunmore & Pike, and others.

A version of our logo is attached for reference; we use it in a variety of color mixes depending on application. Vector available if needed or can be used FPO and our team will replace.

These are our colors, please take note and ignore the 'color' field:

Light Blue: C:66%/M:6%/Y:22%/K:0%; H:189° S:65% B:78%
Light Grey: C:35%/M:26%/Y:24%/K:0%; H:213° S:5% B:70%
Dark Blue: C:90%/M:50%/Y:44%/K:20%; H:189° S:82% B:43%
Dark Grey: C:70%/M:60%/Y:54%/K:38%; H:213° S:11% B:30%

Project Deadline Extended
Reason: Some revisions still outstanding before we can make selection, and some submissions we have agreed to wait for. Please submit all work ASAP so our team can provide feedback to you. Thanks!

Target Market(s)

DIY'ers; home renovators

Industry/Entity Type

Home Improvement

Font styles to use
Sans Serif

Requirements
Must have
• 1. Brand logo w/ logotype
• 2. Brand name without logo (can be on shipping mark side)
• 3. Multi-lingual En/Fr/Es (you do not need to include multi-lingual content but must allow space for our own translations if you do not)
• 4. Shipping/Handling Glyphs on 5 sides (all but bottom)
• i.e. fragile, this way up, team lift or mech lift, clamp or no clamp, max-stack
• 5. Two sides should include a marked 4" x 4" area for affixing labels (e.g. UPC, SSCC, etc.) ideally with a dotted line or corner marks or similar.
• 6. Shipping mark details or space for them (should be on the smallest side, only needed on one but can be on both) [see example file of shipping mark informations]
Nice to have
• Design that can be used either with color label on brown box, or brown box only.
• If designing for color label; please see the sample images included. Lifestyle should be prominent, the inside photo being smaller to help show interior features. These photos are obviously not useful for brown-box design.

```html
<!DOCTYPE html>
<html lang="en">
<head>
<meta charset="utf-8">
<title>Clearmont – Mailer Box Dieline</title>
<link href="https://fonts.googleapis.com/css2?family=Josefin+Sans:wght@400&family=Oswald:wght@400;500&display=swap" rel="stylesheet">
<style>
  :root {
    --backdrop-light: #f4f5f5;
    --backdrop-edge: #e3e4e5;
    --kraft: #b38f74;
    --kraft-flap: #b6957a;
    --dieline: #4a4645;
    --dark-grey: #4b4d52;
    --light-blue: #45b8c8;
    --dark-blue: #1e5f6e;
    --slot: #ffffff;
  }
  html, body {
    margin: 0;
    width: 1200px;
    height: 1200px;
    overflow: hidden;
  }
  body {
    background: radial-gradient(circle at 50% 45%, var(--backdrop-light) 0%, var(--backdrop-edge) 75%);
  }
  .dieline { display: block; width: 1200px; height: 1200px; }
  .panel { fill: var(--kraft); stroke: var(--dieline); stroke-width: 0.8; }
  .flap { fill: var(--kraft-flap); stroke: var(--dieline); stroke-width: 0.8; }
  .hand-slot { fill: var(--slot); stroke: var(--dieline); stroke-width: 0.6; }
  .brand-name {
    font-family: "Josefin Sans", sans-serif;
    fill: var(--dark-grey);
    letter-spacing: 0.14em;
  }
  .brand-dot { fill: var(--light-blue); }
  .mark-label {
    font-family: "Oswald", sans-serif;
    fill: var(--dark-grey);
  }
  .mark-bar { fill: var(--dark-blue); }
  .glyph-frame { fill: none; stroke: var(--dark-grey); stroke-width: 0.9; }
  .glyph-line { fill: none; stroke: var(--dark-grey); stroke-width: 1.6; stroke-linecap: round; stroke-linejoin: round; }
  .glyph-fill { fill: var(--dark-grey); }
</style>
</head>
<body>
<svg class="dieline" viewBox="0 0 1200 1200" xmlns="http://www.w3.org/2000/svg">

  <!-- Top tuck flap with rounded ears -->
  <rect class="flap" x="302" y="220" width="596" height="100"/>
  <path class="flap" d="M302 220 L282 220 C232 220 202 255 202 292 L202 306 Q202 320 216 320 L302 320 Z"/>
  <path class="flap" d="M898 220 L918 220 C968 220 998 255 998 292 L998 306 Q998 320 984 320 L898 320 Z"/>

  <!-- Lid -->
  <rect class="panel" x="302" y="320" width="596" height="230"/>
  <path class="flap" d="M302 320 L216 337 Q202 341 202 356 L202 516 Q202 530 216 533 L302 550 Z"/>
  <path class="flap" d="M898 320 L984 337 Q998 341 998 356 L998 516 Q998 530 984 533 L898 550 Z"/>

  <g class="lid-brand">
    <circle class="brand-dot" cx="508" cy="470" r="11"/>
    <text class="brand-name" x="530" y="479" font-size="22">CLEARMONT</text>
  </g>

  <!-- Front panel -->
  <rect class="panel" x="302" y="550" width="596" height="100"/>
  <path class="flap" d="M302 550 L202 552 L202 648 L302 650 Z"/>
  <path class="flap" d="M898 550 L998 552 L998 648 L898 650 Z"/>

  <g class="front-brand">
    <circle class="brand-dot" cx="346" cy="596" r="9"/>
    <text class="brand-name" x="364" y="602" font-size="15">CLEARMONT</text>
  </g>

  <!-- Base with end panels -->
  <rect class="panel" x="302" y="650" width="596" height="229"/>
  <rect class="panel" x="202" y="650" width="100" height="229"/>
  <rect class="panel" x="898" y="650" width="100" height="229"/>
  <path class="flap" d="M202 650 L102 650 L102 710 L98 714 L98 814 L102 818 L102 879 L202 879 Z"/>
  <path class="flap" d="M998 650 L1098 650 L1098 710 L1102 714 L1102 814 L1098 818 L1098 879 L998 879 Z"/>
  <rect class="hand-slot" x="299" y="712" width="7" height="105" rx="3.5"/>
  <rect class="hand-slot" x="894" y="712" width="7" height="105" rx="3.5"/>

  <text class="mark-label" font-size="16" font-weight="500" transform="translate(262 672) rotate(90)">MODEL :</text>
  <text class="mark-label" font-size="16" font-weight="500" transform="translate(240 672) rotate(90)">COLOUR :</text>

  <text class="brand-name" font-size="15" transform="translate(954 843) rotate(-90)">CLEARMONT</text>

  <!-- Back panel -->
  <rect class="panel" x="302" y="879" width="596" height="100"/>
  <path class="flap" d="M302 879 L202 882 L202 977 L302 979 Z"/>
  <path class="flap" d="M898 879 L998 882 L998 977 L898 979 Z"/>

  <g class="handling-glyphs">
    <!-- recycle -->
    <rect class="glyph-frame" x="318" y="913" width="33" height="32"/>
    <path class="glyph-line" d="M334.5 920 L343 934 L326 934 Z"/>
    <!-- this way up -->
    <rect class="glyph-frame" x="353" y="913" width="33" height="32"/>
    <path class="glyph-line" d="M359 919 H380 M364 938 V922 M360 926 L364 922 L368 926 M375 938 V922 M371 926 L375 922 L379 926"/>
    <!-- keep dry -->
    <rect class="glyph-frame" x="388" y="913" width="33" height="32"/>
    <path class="glyph-line" d="M393 930 Q404.5 914 416 930 Z M404.5 930 V939 Q404.5 942 401 940"/>
    <!-- fragile -->
    <rect class="glyph-frame" x="423" y="913" width="33" height="32"/>
    <path class="glyph-line" d="M435 918 H445 M440 918 V926"/>
    <path class="glyph-fill" d="M433 927 H447 V940 H433 Z"/>
    <!-- handle with care -->
    <rect class="glyph-frame" x="458" y="913" width="33" height="32"/>
    <path class="glyph-line" d="M469 924 L474.5 920 L480 924 L474.5 928 Z M464 940 V930 L469 925 M485 940 V930 L480 925"/>
  </g>

  <g class="shipping-mark" transform="rotate(180 600 929)">
    <rect class="mark-bar" x="516" y="903" width="4" height="46"/>
    <text class="mark-label" x="532" y="914" font-size="11">CARTON NUMBER:</text>
    <text class="mark-label" x="532" y="930" font-size="11">CARTON MEASUREMENT :</text>
    <text class="mark-label" x="532" y="946" font-size="11">NET WEIGHT :</text>

    <rect class="mark-bar" x="320" y="903" width="4" height="46"/>
    <text class="mark-label" x="337" y="914" font-size="11">ITEM NUMBER :</text>
    <text class="mark-label" x="337" y="930" font-size="11">DESCRIPTION:</text>
    <text class="mark-label" x="337" y="946" font-size="11">QTY:</text>
  </g>

</svg>
</body>
</html>
```